Laser Hair Removal Tri Fold brochure

I'm looking for a tri fold brochure (A4 size) for a cosmetic surgery centre / dermatology clinic for our laser hair removal services please.

Whilst we are more medical centre than spa, and cater to both men and women, some warmth would good to convey.

I've attached several versions of our logo - either can be used depending on the design style and colouring used. You can see more about us at www.quellmira.ae. I've also added some photos of our clinic if that is of any interest. No need to use them but they're there if you want them.

As we are based in the Middle East, no images showing too much skin should be used. Legs or face, or certain parts of the body are fine, so long as they aren't too revealing, as we need to be culturally sensitive.

One of our (non creative) staff has drafted a basic brochure using Word, which I've attached as a point of reference or for content, although naturally it's not professionally done so it's by no means a design guide! Also open to written content improvement if necessary but this part is non-essential. The only content I specifically want to keep is the price list please.

Many thanks!

Industry/Entity Type

Clinic

```html
<!DOCTYPE html>
<html lang="en">
<head>
<meta charset="utf-8">
<title>Laser Hair Removal – Tri Fold Brochure</title>
<link href="https://fonts.googleapis.com/css2?family=Varela+Round&family=Open+Sans:ital,wght@1,800&display=swap" rel="stylesheet">
<style>
  :root {
    --sky-light: #c4e6f5;
    --sky-mid: #66b6e1;
    --sky-band: #4a9fd2;
    --navy: #0b5a99;
    --navy-deep: #084a82;
    --ink: #1d2a33;
    --white: #ffffff;
    --ring: #5d6670;
    --ring-light: #c9d0d6;
  }
  * { margin: 0; padding: 0; box-sizing: border-box; }
  html, body { width: 1200px; height: 848px; overflow: hidden; background: var(--white); }
  .brochure {
    position: relative; width: 1200px; height: 848px; overflow: hidden;
    font-family: "Varela Round", "Trebuchet MS", sans-serif;
    color: var(--ink);
  }
  .backdrop { position: absolute; inset: 0; }
  .copy {
    position: absolute; font-size: 14.6px; line-height: 20.4px;
    letter-spacing: 0.35px; text-align: justify;
  }
  .intro-copy { left: 24px; top: 31px; width: 357px; }
  .visit-copy { left: 821px; top: 214px; width: 359px; }
  .how-heading {
    position: absolute; left: 420px; top: 444px;
    font-family: "Open Sans", Arial, sans-serif; font-style: italic; font-weight: 800;
    font-size: 29px; color: #e4f3fb; letter-spacing: 0.2px;
  }
  .how-copy { left: 421px; top: 511px; width: 344px; color: var(--white); }
  .photo { position: absolute; }
  .doctor-photo {
    left: 400px; top: 0; width: 400px; height: 358px;
    background: linear-gradient(135deg, #e9eef2 0%, #f7f9fb 45%, #dfe6ec 100%);
  }
  .treatment-photo {
    left: 800px; top: 380px; width: 400px; height: 262px;
    background: radial-gradient(ellipse at 40% 40%, #c8612a 0%, #8d3317 55%, #4a1a0d 100%);
    clip-path: path("M0 12 Q 200 -8 400 48 V262 H0 Z");
  }
  .circle-photo {
    border-radius: 50%;
    background: linear-gradient(160deg, #f4f4f4 0%, #e3e0dc 60%, #c9bfb6 100%);
    border: 9px solid var(--ring);
    box-shadow: 0 0 0 3px var(--ring-light), 0 4px 10px rgba(0,0,0,0.35);
  }
  .circle-large { left: 26px; top: 288px; width: 272px; height: 272px; }
  .circle-small { left: 144px; top: 487px; width: 218px; height: 218px; }
  .lotus-mark {
    position: absolute; left: 920px; top: 686px; width: 162px; height: 112px;
    background: radial-gradient(ellipse at 50% 60%, #b8b3ec 0%, rgba(196,230,245,0) 70%);
  }
</style>
</head>
<body>
<div class="brochure">
  <svg class="backdrop" width="1200" height="848" viewBox="0 0 1200 848" aria-hidden="true">
    <!-- left panel -->
    <rect x="0" y="0" width="400" height="848" fill="var(--sky-light)"/>
    <path d="M0 0 H400 V212 Q200 320 0 500 Z" fill="var(--sky-mid)"/>
    <path d="M0 500 Q200 320 400 212 V226 Q200 336 0 514 Z" fill="var(--white)"/>
    <path d="M0 514 Q200 336 400 226 V300 Q200 400 0 566 Z" fill="var(--sky-band)"/>
    <path d="M0 566 Q200 400 400 300 V312 Q200 412 0 578 Z" fill="#e8f5fb"/>
    <!-- centre panel -->
    <rect x="400" y="358" width="400" height="490" fill="var(--navy)"/>
    <path d="M400 358 H800 V380 Q600 372 400 404 Z" fill="var(--navy-deep)"/>
    <path d="M400 404 Q600 372 800 380 V386 Q600 380 400 410 Z" fill="#2d7cbc"/>
    <!-- right panel -->
    <rect x="800" y="0" width="400" height="848" fill="var(--sky-light)"/>
    <path d="M800 0 H1110 Q960 60 800 110 Z" fill="#3f96cf"/>
    <path d="M800 118 Q990 40 1200 20 V110 Q1000 130 800 182 Z" fill="#5aace0"/>
    <path d="M800 182 Q1000 130 1200 110 V122 Q1000 142 800 194 Z" fill="#eef8fc"/>
    <path d="M800 380 Q1000 366 1200 420 V432 Q1000 380 800 392 Z" fill="#5aace0"/>
  </svg>

  <p class="copy intro-copy">Laser hair removal is becoming more and more mainstream with women as well as men; it is one of the most popular aesthetic treatments in practices all over the world. No one really wants to have more discomfort, ingrown hair and irritated or infected skin, which is the usual consequence of shaving, plucking, waxing... Laser hair removal is a long-lasting, comfortable solution!</p>

  <div class="photo circle-photo circle-large" role="img" aria-label="Photo of a man in protective goggles receiving laser treatment on his face"></div>
  <div class="photo circle-photo circle-small" role="img" aria-label="Photo of a woman in protective goggles receiving laser treatment on her jaw"></div>

  <div class="photo doctor-photo" role="img" aria-label="Photo of a smiling doctor in a white coat with a stethoscope"></div>

  <h2 class="how-heading">How It Works</h2>
  <p class="copy how-copy">The deep penetration of ‘Nd:YAG’ laser ensures it reaches even the deepest follicles, permanently removing those unwanted hair, while its low absorption in all skin types ensures the surrounding tissue is preserved. This guarantees safe, fast and effective hair removal, even in the darkest skin types. Medical studies show our treatment to be gentle on the epidermal layer unlike other laser hair removal treatments. The procedure is quick and pain-free and you will begin to see results immediately, and within 4 treatments, permantely removed the unwanted hair.</p>

  <p class="copy visit-copy">Come visit our clinic that is beatifully decorated with a spa like atmostphere and relax as you are in the hands of trained professionals that keeps the utmost of care for you and your concerns. Or, you can call us on +971 2 555 0148 and chat to us about any queries you may have.</p>

  <div class="photo treatment-photo" role="img" aria-label="Photo of a warmly lit treatment room with a massage bed, towels and equipment"></div>

  <div class="lotus-mark" role="img" aria-label="Decorative lotus ornament"></div>
</div>
</body>
</html>
```